odrin stationery

we have a logo and it is in the upload files. Please use the logos in denatured color effect from the same color pantone.
We would like to see a stationery design for a new company working worldwide in the petrochemical sector as an agent.
Please use our logo to create business card, presentation folder, letterhead, envelope,note pad, note books etc etc.
Of course we want convey security and stability, in terms of finance and connections

Target Market(s)

Multinational enterprise, executive, professional,

Industry/Entity Type

Business

Font styles to use
Serif

Colors
0756a3
3176b5
85acd3
86cae6
87c9e5
33a6d7
0692cd

Requirements
Must have
• business cards must have option for address name, title, email telephone etc. I like business card that is both side.

Color as I stated DESAUTERED color effect based on the original color,

I LIKE MATTE effect
Nice to have
• all the pieces must be cohesive. I like print raised for business cards
Should not have
• Shiny finish

```html
<!DOCTYPE html>
<html lang="en">
<head>
<meta charset="utf-8">
<title>Odrin Trading Service – Business Card</title>
<link rel="stylesheet" href="https://fonts.googleapis.com/css2?family=Didact+Gothic&family=Questrial&display=swap">
<style>
  :root {
    --bg: #e6e6ea;
    --navy: #184c97;
    --navy-soft: #3176b5;
    --sky: #85acd3;
    --paper: #f7f8fa;
    --ink: #1f1f24;
    --rule: #c9ccd2;
  }
  * { box-sizing: border-box; margin: 0; padding: 0; }
  html, body {
    width: 1200px; height: 934px; overflow: hidden;
    background: var(--bg);
    font-family: "Didact Gothic", "Questrial", sans-serif;
    color: var(--ink);
  }
  .stage {
    position: relative; width: 1200px; height: 934px;
    display: flex; align-items: center; justify-content: center; gap: 60px;
  }
  .card {
    position: relative; width: 525px; height: 300px;
    box-shadow: 0 10px 26px rgba(30, 40, 70, 0.16);
    overflow: hidden;
  }
  /* front side */
  .card--front {
    background: var(--navy);
    display: flex; align-items: center; justify-content: center;
  }
  .wordmark {
    display: flex; align-items: center; gap: 14px;
  }
  .wordmark__dot {
    width: 54px; height: 54px; border-radius: 50%;
    border: 2px solid currentColor;
  }
  .wordmark__name {
    font-family: "Didact Gothic", sans-serif;
    font-size: 30px; letter-spacing: 0.02em; white-space: nowrap;
  }
  .card--front .wordmark { color: #ffffff; }
  /* back side */
  .card--back { background: var(--paper); }
  .card--back .wordmark {
    position: absolute; left: 34px; top: 170px; color: var(--navy);
  }
  .card--back .wordmark__dot { width: 44px; height: 44px; }
  .card--back .wordmark__name { font-size: 23px; }
  .contact {
    position: absolute; left: 300px; top: 40px;
    font-size: 14px; line-height: 1.45;
  }
  .contact__name {
    font-family: "Questrial", sans-serif; font-weight: 700;
    font-size: 17px; letter-spacing: 0.04em; text-transform: uppercase;
  }
  .contact__title { margin: 0 0 12px 10px; font-size: 14px; }
  .contact__list { list-style: none; margin-left: 22px; }
  .contact__item { display: flex; align-items: center; gap: 8px; height: 20px; }
  .contact__icon { width: 15px; height: 15px; flex: none; color: var(--navy); }
  .contact__address { margin: 18px 0 0 50px; font-size: 14px; line-height: 1.4; }
  .band {
    position: absolute; left: 0; right: 0; bottom: 0; height: 22px;
    background: var(--navy);
    border-top: 5px solid var(--rule);
  }
</style>
</head>
<body>
<main class="stage">
  <section class="card card--front" aria-label="Business card front">
    <div class="wordmark">
      <span class="wordmark__dot"></span>
      <span class="wordmark__name">Odrin Trading Service</span>
    </div>
  </section>

  <section class="card card--back" aria-label="Business card back">
    <div class="wordmark">
      <span class="wordmark__dot"></span>
      <span class="wordmark__name">Odrin Trading Service</span>
    </div>

    <div class="contact">
      <p class="contact__name">Marko Lenard</p>
      <p class="contact__title">General Manager</p>
      <ul class="contact__list">
        <li class="contact__item">
          <svg class="contact__icon" viewBox="0 0 16 16" aria-hidden="true"><circle cx="8" cy="8" r="7" fill="none" stroke="currentColor" stroke-width="1.3"/><path d="M5.5 4.5l1.5 0 .6 1.8-1 .8a5 5 0 0 0 2.3 2.3l.8-1 1.8.6 0 1.5c-3.5.3-6.3-2.5-6-6z" fill="currentColor"/></svg>
          +385 1 40 20 318
        </li>
        <li class="contact__item">
          <svg class="contact__icon" viewBox="0 0 16 16" aria-hidden="true"><circle cx="8" cy="8" r="7" fill="none" stroke="currentColor" stroke-width="1.3"/><rect x="5" y="4.5" width="6" height="2.5" fill="currentColor"/><rect x="4" y="7" width="8" height="3.5" rx=".6" fill="currentColor"/><rect x="5.5" y="9.5" width="5" height="2" fill="#fff" stroke="currentColor" stroke-width=".6"/></svg>
          +385 1 40 20 319
        </li>
        <li class="contact__item">
          <svg class="contact__icon" viewBox="0 0 16 16" aria-hidden="true"><circle cx="8" cy="8" r="7" fill="none" stroke="currentColor" stroke-width="1.3"/><rect x="4" y="5.5" width="8" height="5.5" fill="currentColor"/><path d="M4 5.5l4 3 4-3" fill="none" stroke="#fff" stroke-width=".8"/></svg>
          info@odrints.com
        </li>
        <li class="contact__item">
          <svg class="contact__icon" viewBox="0 0 16 16" aria-hidden="true"><circle cx="8" cy="8" r="7" fill="none" stroke="currentColor" stroke-width="1.3"/><ellipse cx="8" cy="8" rx="3" ry="7" fill="none" stroke="currentColor" stroke-width="1"/><path d="M1 8h14M2.2 4.5h11.6M2.2 11.5h11.6" stroke="currentColor" stroke-width="1"/></svg>
          www.odrints.com
        </li>
      </ul>
      <p class="contact__address">Lipa 12c, Sesvete<br>10 360 ZAGREB</p>
    </div>

    <div class="band"></div>
  </section>
</main>
</body>
</html>
```